Harlow Ridgeway a PlateWork Fabricator! Pressure Vessels, Stainless Vessels, Steel Fabricator!

Update and modernize the www.harlowridgeway.example website. Basically throwing away the old site and coming back with a new feel, new look, but some of the same content. One of our other companies is www.brantwickbuild.example and if you view that site you will get a idea of how we would like the site to feel. Below are the HR logos and the colors are #231F20 and #6D0B17 and the font is Ethnocentric Rg.

Target Market(s)

Steel Fabrication, Platework, Vessel Fabrication,

Industry/Entity Type

Steel

Coding

Coded - Design and coding required

Number of Pages Required

5+ page

Font styles to use
Other font styles liked:
• Ethnocentric Rg

Requirements
Must have
• Industry feel... site must flow and color scheme and font be consistent.

```html
<!DOCTYPE html>
<html lang="en">
<head>
<meta charset="utf-8">
<title>Harlow Ridgeway — Fabrication Services</title>
<link rel="stylesheet" href="https://fonts.googleapis.com/css2?family=Montserrat:wght@300;400;500&family=Roboto+Condensed:wght@400;700&family=Source+Sans+3:wght@400;600&display=swap">
<style>
  :root {
    --ink: #231F20;
    --brand-red: #6D0B17;
    --heading-red: #7a0c18;
    --accent-yellow: #f8c600;
    --nav-slate: #3f4e5c;
    --footer-grey: #626366;
    --white: #ffffff;
  }
  * { box-sizing: border-box; margin: 0; padding: 0; }
  html, body { width: 1200px; height: 1120px; overflow: hidden; }
  body { position: relative; background: var(--white); color: var(--ink); font-family: "Montserrat", sans-serif; }

  /* Header */
  .site-header { position: absolute; left: 0; top: 0; width: 1200px; height: 127px; background: var(--white); }
  .brand { position: absolute; left: 50px; top: 35px; display: flex; align-items: center; gap: 10px; text-decoration: none; }
  .brand-mark { width: 70px; height: 70px; border-radius: 50%; background: var(--brand-red); }
  .brand-name { font-family: "Montserrat", sans-serif; font-weight: 500; font-size: 21px; line-height: 1; color: var(--ink); text-transform: uppercase; letter-spacing: 0.5px; }
  .contact-line { position: absolute; left: 1001px; top: 44px; font-family: "Roboto Condensed", sans-serif; font-size: 11px; color: var(--nav-slate); }
  .contact-line .divider { margin-left: 8px; }
  .main-nav { position: absolute; right: 42px; top: 70px; display: flex; gap: 17px; }
  .main-nav a { font-family: "Roboto Condensed", sans-serif; font-size: 18px; color: var(--nav-slate); text-decoration: none; text-transform: uppercase; }

  /* Hero */
  .hero { position: absolute; left: 0; top: 127px; width: 1200px; height: 416px; overflow: hidden; }
  .hero-photo { position: absolute; inset: 0;
    background:
      radial-gradient(ellipse 220px 180px at 560px 230px, rgba(255,245,245,0.95), rgba(255,220,220,0) 70%),
      linear-gradient(90deg, #2f4f8a 0%, #8a7e98 25%, #d98f88 42%, #efe3ea 52%, #3f6fc8 68%, #1e52c0 85%, #2b5fcf 100%); }
  .hero-copy { position: absolute; left: 51px; top: 79px; }
  .hero-kicker { font-weight: 400; font-size: 36px; line-height: 1; color: var(--accent-yellow); letter-spacing: 1px; }
  .hero-sub { margin-top: 8px; font-weight: 400; font-size: 19px; line-height: 1; color: var(--accent-yellow); letter-spacing: 0.5px; }
  .hero-title { margin-top: 10px; font-weight: 300; font-size: 49px; line-height: 48px; color: var(--white); letter-spacing: 2px; }
  .btn { display: inline-flex; align-items: center; justify-content: center; background: var(--accent-yellow); color: var(--ink); font-family: "Montserrat", sans-serif; font-weight: 500; text-transform: uppercase; text-decoration: none; letter-spacing: 0.5px; }
  .hero .btn { position: absolute; left: 51px; top: 269px; width: 171px; height: 38px; font-size: 14px; border: 1px solid var(--white); }

  /* Quality section */
  .quality { position: absolute; left: 0; top: 543px; width: 1200px; height: 259px; background: var(--white); }
  .quality-photo { position: absolute; left: 0; top: 0; width: 486px; height: 259px;
    background: linear-gradient(150deg, rgba(255,255,255,0) 20%, #b9bcc0 40%, #6e7175 60%, #2d2f33 80%, #8d9094 100%);
    clip-path: polygon(0 55%, 60% 0, 100% 55%, 100% 100%, 0 100%); }
  .quality-copy { position: absolute; left: 557px; top: 41px; width: 345px; }
  .section-heading { font-family: "Montserrat", sans-serif; font-weight: 500; font-size: 15px; line-height: 1; color: var(--heading-red); letter-spacing: 0.9px; text-transform: uppercase; white-space: nowrap; }
  .quality-copy p { margin-top: 11px; font-weight: 300; font-size: 10.8px; line-height: 19.2px; color: var(--ink); }
  .quality-actions { margin-top: 11px; margin-left: -1px; display: flex; gap: 16px; }
  .quality-actions .btn { width: 110px; height: 30px; font-size: 12px; font-weight: 400; }

  /* Size section */
  .reach { position: absolute; left: 0; top: 802px; width: 1200px; height: 238px; overflow: hidden; }
  .reach-photo { position: absolute; inset: 0;
    background:
      radial-gradient(ellipse 260px 230px at 1060px 150px, #f4f5f7 55%, rgba(244,245,247,0) 75%),
      linear-gradient(180deg, #e9e6e6 0%, #ddd6d2 45%, #c9c2bd 75%, #d8d3d0 100%); }
  .reach-copy { position: absolute; left: 211px; top: 45px; width: 610px; }
  .reach-heading { font-family: "Roboto Condensed", sans-serif; font-weight: 700; font-size: 24px; color: var(--heading-red); text-transform: uppercase; }
  .reach-copy p { margin-top: 10px; font-family: "Source Sans 3", sans-serif; font-size: 10.6px; line-height: 17.6px; color: var(--ink); }
  .reach .btn { position: absolute; left: 209px; top: 157px; width: 132px; height: 34px; font-size: 13px; font-weight: 400; border: 1px solid var(--white); }

  /* Footer */
  .site-footer { position: absolute; left: 0; top: 1040px; width: 1200px; height: 80px; background: var(--footer-grey); color: var(--white); font-family: "Source Sans 3", sans-serif; }
  .copyright { position: absolute; left: 192px; top: 18px; font-size: 10.5px; font-weight: 600; text-transform: uppercase; }
  .footer-links { position: absolute; left: 192px; top: 35px; font-size: 10.5px; font-weight: 600; }
  .footer-links a { color: var(--white); text-decoration: none; }
  .social-links { position: absolute; left: 898px; top: 24px; display: flex; gap: 20px; }
  .social-dot { width: 15px; height: 15px; border-radius: 50%; background: #c9cacc; }
</style>
</head>
<body>
  <header class="site-header">
    <a class="brand" href="#">
      <span class="brand-mark"></span>
      <span class="brand-name">Harlow Ridgeway</span>
    </a>
    <div class="contact-line">P: 1-800-555-0142 <span class="divider">I</span></div>
    <nav class="main-nav">
      <a href="#">Home</a>
      <a href="#">Products</a>
      <a href="#">Services</a>
      <a href="#">Benefits</a>
      <a href="#">Support</a>
      <a href="#">Blog</a>
      <a href="#">Sign In</a>
    </nav>
  </header>

  <section class="hero">
    <div class="hero-photo" role="img" aria-label="Welder in blue protective gear cutting steel with sparks flying"></div>
    <div class="hero-copy">
      <p class="hero-kicker">YOUR VISION</p>
      <p class="hero-sub">OUR CUSTOM QUALITY</p>
      <h1 class="hero-title">FABRICATION<br>SERVICES</h1>
    </div>
    <a class="btn" href="#">View Product</a>
  </section>

  <section class="quality">
    <div class="quality-photo" role="img" aria-label="Stack of polished steel pipes"></div>
    <div class="quality-copy">
      <h2 class="section-heading">Quality Assurance Guaranteed</h2>
      <p>As experienced steel fabricators, we anticipate your needs and requirements from vision to production to delivery. Your steel fabrication products are manufactured by proven business processes and some of the industry’s</p>
      <div class="quality-actions">
        <a class="btn" href="#">Products</a>
        <a class="btn" href="#">Services</a>
      </div>
    </div>
  </section>

  <section class="reach">
    <div class="reach-photo" role="img" aria-label="Large white industrial pipeline stretching into the distance"></div>
    <div class="reach-copy">
      <h2 class="reach-heading">Success at Any Size</h2>
      <p>We deliver fabrication solutions from small scale projects to our specialized oversized and overweight fabrication, processing, and handling capabilities. Steel fabricators proudly serving the power generation, water treatment, waste treatment, agriculture, chemical, food processing, mining, oil &amp; gas and heavy industry project sectors for nearly 40 years.</p>
    </div>
    <a class="btn" href="#">Who We Serve</a>
  </section>

  <footer class="site-footer">
    <p class="copyright">© 2018 Harlow Ridgeway</p>
    <p class="footer-links"><a href="#">Home</a> - <a href="#">Site Map</a> – <a href="#">FAQ</a> – <a href="#">Privacy Policy</a> – <a href="#">Terms of Use</a> – <a href="#">Contact Us</a></p>
    <div class="social-links" aria-label="Social links">
      <span class="social-dot"></span>
      <span class="social-dot"></span>
      <span class="social-dot"></span>
      <span class="social-dot"></span>
    </div>
  </footer>
</body>
</html>
```